"Vine Hollow Excursions" is a top notch Santa Barbara County Wine Tour company.

We provide scenic, boutique and custom wine tours. I need the card to be clean and classy. I will provide our logo. I would like the logo to cover the back side of the card as an option and would like to see a couple color options other then our signature green and gold. I would like to see some creative options and let the designers come up with options.
I need cards for myself and my team. The final design should communicate "An authentic and boutique wine tour experience"
Please use my website for reference www.vinehollowexcursions.example

Target Market(s)

We have a wide range of clients from millennials to baby boomers

Industry/Entity Type

Tour

Contact Information for Business Card

Contact info:
Dale Marsh
805-218-6390
info@vinehollowexcursions.example
vinehollowexcursions.example

Colors

Designer to choose colors to be used in the design.

Requirements
Must have
• my logo
Nice to have
• *I would like to have the backside side with the logo and the company statement
• "An authentic and boutique wine tour experience" as an option.
• *I would also like to see what the designers can create!
• *I would like to see an option that incorporates or social: pixgram, rantly, journey guide
Should not have
• I do not want it too busy.

```html
<!DOCTYPE html>
<html lang="en">
<head>
<meta charset="utf-8">
<title>Vine Hollow Excursions – Business Card</title>
<link href="https://fonts.googleapis.com/css2?family=Cinzel:wght@400;600&family=Open+Sans:wght@400;700&display=swap" rel="stylesheet">
<style>
  :root{
    --canvas:#e7e7e9;
    --card:#ffffff;
    --green:#1f6b40;
    --green-dark:#185634;
    --green-bright:#7cc243;
    --green-pale:#cfe6b3;
    --gold-a:#c99d2e;
    --gold-b:#f5d770;
    --taupe:#a68a64;
    --text-soft:#3e6a52;
    --rule:#b9cbbf;
    --mist:#eef2ef;
  }
  html,body{margin:0;height:100%;overflow:hidden;}
  body{
    width:1200px;height:1200px;background:var(--canvas);
    position:relative;
  }
  .card{
    position:absolute;left:170px;width:860px;height:491px;
    background:var(--card);
    box-shadow:0 6px 18px rgba(0,0,0,.12);
  }
  .card--front{top:60px;}
  .card--back{top:640px;}
  .card svg{display:block;width:100%;height:100%;}
  .logo-name{font-family:"Cinzel",serif;font-weight:400;fill:var(--taupe);letter-spacing:2px;}
  .social-label{font-family:"Open Sans",sans-serif;font-size:10px;fill:var(--green);font-weight:400;}
  .site{font-family:"Open Sans",sans-serif;font-size:15px;fill:var(--text-soft);}
  .person{font-family:"Cinzel",serif;font-weight:400;fill:var(--green);font-size:34px;}
  .contact-head{font-family:"Open Sans",sans-serif;font-weight:700;fill:var(--green);font-size:21px;}
  .contact-line{font-family:"Open Sans",sans-serif;font-weight:400;fill:var(--text-soft);font-size:18px;}
  .phone{font-family:"Open Sans",sans-serif;font-weight:400;fill:var(--green);font-size:34px;}
</style>
</head>
<body>

<!-- Logo side -->
<div class="card card--front">
  <svg viewBox="0 0 860 491" xmlns="http://www.w3.org/2000/svg">
    <defs>
      <linearGradient id="gold" x1="0" x2="1" y1="0" y2="0">
        <stop offset="0" stop-color="var(--gold-a)"/>
        <stop offset=".5" stop-color="var(--gold-b)"/>
        <stop offset="1" stop-color="var(--gold-a)"/>
      </linearGradient>
      <radialGradient id="mistFront" cx=".7" cy=".75" r=".7">
        <stop offset="0" stop-color="var(--mist)"/>
        <stop offset="1" stop-color="#ffffff" stop-opacity="0"/>
      </radialGradient>
    </defs>

    <rect class="vineyard-backdrop" x="180" y="120" width="680" height="371" fill="url(#mistFront)" role="img" aria-label="Faint vineyard rows and sunburst backdrop"/>

    <path class="gold-bar" d="M268 0 H640 V12 H278 Q268 12 268 4 Z" fill="url(#gold)"/>

    <rect class="band band--right-accent" x="590" y="190" width="50" height="48" fill="var(--green-bright)"/>
    <rect class="band band--right" x="640" y="190" width="220" height="48" fill="var(--green)"/>

    <rect class="band band--left" x="0" y="375" width="290" height="48" fill="var(--green)"/>
    <rect class="band band--left-accent" x="290" y="375" width="48" height="48" fill="var(--green-pale)"/>

    <rect class="edge-pill edge-pill--gold" x="0" y="240" width="40" height="8" rx="4" fill="url(#gold)"/>
    <rect class="edge-pill edge-pill--green" x="0" y="254" width="40" height="8" rx="4" fill="var(--green)"/>

    <text class="logo-name" x="430" y="128" text-anchor="middle" font-size="42">Vine Hollow</text>
    <text class="logo-name" x="430" y="176" text-anchor="middle" font-size="42">Excursions</text>

    <g class="social-bar" transform="translate(280 300)">
      <rect width="300" height="44" fill="#fff" stroke="var(--green-pale)" stroke-width="2"/>
      <g stroke="var(--green-bright)" stroke-width="2">
        <line x1="60" y1="8" x2="60" y2="36"/>
        <line x1="120" y1="8" x2="120" y2="36"/>
        <line x1="180" y1="8" x2="180" y2="36"/>
        <line x1="240" y1="8" x2="240" y2="36"/>
      </g>
      <text class="social-label" x="30" y="26" text-anchor="middle">Circlenet</text>
      <text class="social-label" x="90" y="26" text-anchor="middle">Chirpy</text>
      <text class="social-label" x="150" y="26" text-anchor="middle">Friendsy</text>
      <text class="social-label" x="210" y="26" text-anchor="middle">rantly</text>
      <text class="social-label" x="270" y="26" text-anchor="middle">pixgram</text>
    </g>

    <text class="site" x="430" y="372" text-anchor="middle">vinehollowexcursions.example</text>
  </svg>
</div>

<!-- Contact side -->
<div class="card card--back">
  <svg viewBox="0 0 860 491" xmlns="http://www.w3.org/2000/svg">
    <defs>
      <linearGradient id="gold2" x1="0" x2="1" y1="0" y2="0">
        <stop offset="0" stop-color="var(--gold-a)"/>
        <stop offset=".5" stop-color="var(--gold-b)"/>
        <stop offset="1" stop-color="var(--gold-a)"/>
      </linearGradient>
      <radialGradient id="mistBack" cx=".72" cy=".6" r=".6">
        <stop offset="0" stop-color="var(--mist)"/>
        <stop offset="1" stop-color="#ffffff" stop-opacity="0"/>
      </radialGradient>
    </defs>

    <rect class="vineyard-backdrop" x="300" y="60" width="560" height="431" fill="url(#mistBack)" role="img" aria-label="Faint vineyard rows and sunburst backdrop"/>

    <path class="corner corner--top" d="M0 0 H330 Q318 18 292 22 L34 58 Q10 62 0 84 Z" fill="var(--green)"/>
    <path class="corner-trim" d="M330 0 Q318 18 292 22 L34 58 Q10 62 0 84" fill="none" stroke="url(#gold2)" stroke-width="5"/>

    <path class="corner corner--bottom" d="M630 491 Q640 452 676 446 L860 416 V491 Z" fill="var(--green)"/>
    <path class="corner-trim" d="M630 491 Q640 452 676 446 L860 416" fill="none" stroke="url(#gold2)" stroke-width="5"/>

    <rect class="edge-mark" x="0" y="190" width="22" height="22" fill="var(--green)"/>
    <rect class="edge-mark" x="0" y="420" width="22" height="22" fill="var(--green)"/>

    <text class="logo-name" x="690" y="120" text-anchor="middle" font-size="34">Vine Hollow</text>
    <text class="logo-name" x="690" y="162" text-anchor="middle" font-size="34">Excursions</text>

    <line x1="40" y1="150" x2="430" y2="150" stroke="var(--rule)" stroke-width="1.5"/>
    <text class="person" x="40" y="205">Dale Marsh</text>
    <line x1="40" y1="225" x2="430" y2="225" stroke="var(--rule)" stroke-width="1.5"/>

    <text class="contact-head" x="60" y="272">Contact:</text>
    <text class="contact-line" x="80" y="300">info@vinehollowexcursions.example</text>
    <text class="contact-line" x="80" y="324">vinehollowexcursions.example</text>

    <line x1="40" y1="352" x2="520" y2="352" stroke="var(--rule)" stroke-width="1.5"/>

    <g class="phone-icon" transform="translate(60 398)">
      <circle r="15" fill="none" stroke="var(--green)" stroke-width="3"/>
      <path d="M-6 -7 Q-8 2 0 7 Q4 9 7 6 L4 2 L1 4 Q-3 1 -3 -3 L-1 -5 Z" fill="var(--green)"/>
    </g>
    <text class="phone" x="86" y="410">805-218-6390</text>
  </svg>
</div>

</body>
</html>
```